Tov Fest Falcons

We are party planning business. We are a team of established individuals and business in party stream businesses like DJ, Caterers, Party supplies, Kids parties, Events & Private Parties and much more. So basically me and business collaborate a team of business or individuals to do clients party in the best way possible.

Target Market(s)

majority of them 16 to 30 -60% to 70 % and 30 to 40 year olds- 30% to 40 %

Industry/Entity Type

Party Planning

Contact Information for Business Card

Tov
Owner & Manager
0481927354
tovfestfalcons@mailbright.example

Requirements
Must have
• front side : Logo and list of services we provide
DJ's, Catering,All party supplies, Tinyvolta and more...just to show what the business is about when anyone looks at the card and at the rear side my details which are already provided.
Should not have
• Dont make it look we do kids party which is just one of the things we do but don't make my business card look like kids party specialist make it more connecting to youngsters and older crowd more

```html
<!DOCTYPE html>
<html lang="en">
<head>
<meta charset="UTF-8">
<title>Tov Fest Falcons – Business Card</title>
<link href="https://fonts.googleapis.com/css2?family=Almendra:wght@700&family=Open+Sans:wght@400;600;700&display=swap" rel="stylesheet">
<style>
  :root {
    --page-bg: #ece9e4;
    --card-light: #ffffff;
    --card-dark: #1d1d1d;
    --ink: #1a1a1a;
    --ink-soft: #333333;
    --accent-red: #d3262b;
    --bone: #e9e2d2;
    --on-dark: #ffffff;
  }
  * { margin: 0; padding: 0; box-sizing: border-box; }
  html, body {
    width: 1200px;
    height: 800px;
    overflow: hidden;
    background: var(--page-bg);
  }
  .canvas {
    width: 1200px;
    height: 800px;
    display: flex;
    justify-content: center;
    align-items: center;
    gap: 60px;
  }
  .card {
    width: 400px;
    height: 640px;
    border-radius: 14px;
    display: flex;
    flex-direction: column;
    align-items: center;
    box-shadow: 0 8px 22px rgba(0,0,0,0.18);
    font-family: "Open Sans", Arial, sans-serif;
    text-align: center;
  }
  .card--details { background: var(--card-light); color: var(--ink); padding: 34px 30px 40px; }
  .card--services { background: var(--card-dark); color: var(--on-dark); padding: 36px 30px 48px; }

  .emblem-art {
    border-radius: 50%;
    flex-shrink: 0;
  }
  .card--details .emblem-art {
    width: 270px;
    height: 250px;
    background: radial-gradient(circle at 55% 40%, var(--bone) 0 30%, rgba(211,38,43,0.55) 31% 45%, rgba(211,38,43,0.12) 46% 68%, rgba(26,26,26,0.08) 69% 100%);
  }
  .card--services .emblem-art {
    width: 300px;
    height: 300px;
    background: radial-gradient(circle at 55% 45%, var(--bone) 0 32%, rgba(211,38,43,0.75) 33% 48%, rgba(211,38,43,0.18) 49% 68%, rgba(255,255,255,0.05) 69% 100%);
  }

  .brand-name {
    display: flex;
    align-items: center;
    gap: 10px;
    font-weight: 700;
    font-size: 34px;
    line-height: 1.05;
    color: var(--accent-red);
    text-transform: uppercase;
    letter-spacing: 1px;
  }
  .card--details .brand-name { margin-top: -6px; }
  .card--services .brand-name { margin-top: 10px; }
  .brand-mark {
    width: 18px;
    height: 18px;
    border-radius: 50%;
    background: var(--accent-red);
    flex-shrink: 0;
  }

  .tagline {
    margin-top: 10px;
    font-family: "Almendra", Georgia, serif;
    font-weight: 700;
    font-size: 20px;
    line-height: 1.15;
    color: var(--ink-soft);
  }

  .contact {
    margin-top: auto;
    display: flex;
    flex-direction: column;
    align-items: center;
  }
  .contact__name { font-weight: 700; font-size: 21px; }
  .contact__role { font-size: 15px; margin-top: 2px; color: var(--ink-soft); }
  .contact__rule {
    width: 210px;
    height: 3px;
    background: var(--ink);
    margin: 12px 0;
    border-radius: 2px;
  }
  .contact__phone { font-size: 17px; }
  .contact__email { margin-top: 10px; font-size: 15px; }

  .services {
    list-style: none;
    margin-top: 22px;
    font-size: 20px;
    line-height: 1.5;
  }
</style>
</head>
<body>
<main class="canvas">
  <section class="card card--details" aria-label="Contact side">
    <div class="emblem-art" role="img" aria-label="Brand illustration with star ring and music notes"></div>
    <p class="brand-name"><span class="brand-mark"></span>Tov Fest<br>Falcons</p>
    <p class="tagline">Delivering The Ultimate<br>Treasures To Your Party</p>
    <div class="contact">
      <p class="contact__name">Tov</p>
      <p class="contact__role">Owner &amp; Manager</p>
      <span class="contact__rule" aria-hidden="true"></span>
      <p class="contact__phone">0481927354</p>
      <p class="contact__email">tovfestfalcons@mailbright.example</p>
    </div>
  </section>

  <section class="card card--services" aria-label="Services side">
    <div class="emblem-art" role="img" aria-label="Brand illustration with music notes"></div>
    <p class="brand-name"><span class="brand-mark"></span>Tov Fest<br>Falcons</p>
    <ul class="services">
      <li>DJ’s</li>
      <li>Catering</li>
      <li>All Party Supplies</li>
      <li>Tinyvolta</li>
      <li>Private parties</li>
    </ul>
  </section>
</main>
</body>
</html>
```